Beachfront Resort Landing Page

I need a design for a landing page related to a Beachfront Costa Rican Resort. This will be used as a Social Media landing page, so conversion is a must. Prefer someone with experience designing single-landing pages for conversions.

Can use this site as a reference for content / info - brisamarena.com

The landing page needs to contain these items

"Book a 4 night Stay During the Costa Rican Green-Season, and get your 5th night Free at this All Inclusive Luxury Beachfront Resort!"

"As a Bonus, we'll throw in any of these Activities or Tours for Free! Don't wait! These will fill up fast."
"Free Massage"
"Night Hike"
"Birdwatching Tour"
"Max 2 per booking, can mix-match. While supplies last. Must redeemed during this stay" (in small print under text / images)

Also highlight these items too please

"Accessible only via boat, this Costa Rican Luxury Paradise is perfect for those wanting to escape the crowds, enjoy amazing cuisine, while swimming in our beachfront pool, and more"

"Green Season is known for whale migrations, enjoy watching the marine life from our beachfront location, or up close and personal via kayak or paddleboard"

"Paddleboards, kayaks, snorkeling gear, and more are free during your stay."

"Enjoy fresh cuisine and unique beverages daily"

"Skyvane Internet Access Included with all Bookings"

The landing page must have
- A contact form close to above the fold area
- Booking dates function around the same area
- CTA's related to most of whats mentioned above
- Can use images from the real site - brisamarena.com
- Areas for videos on the landing page
- Must resemble a good landing page design for conversion, not a standard web-page. Those who know, will know.

Please let me know if you have any questions.

```html
<!DOCTYPE html>
<html lang="en">
<head>
<meta charset="UTF-8">
<title>Brisa Marena — Green Season Offer</title>
<link rel="stylesheet" href="https://fonts.googleapis.com/css2?family=Plus+Jakarta+Sans:wght@300;400;500;600;700;800&display=swap">
<style>
:root{
  --green:#2f7a36;
  --green-dark:#2d6a33;
  --green-deep:#3a6b40;
  --green-foot:#4d7b53;
  --ink:#2a2a2a;
  --muted:#6b6b6b;
  --paper:#f4f4f2;
  --white:#ffffff;
  --star:#e24b3b;
}
*{box-sizing:border-box;margin:0;padding:0}
html,body{width:1200px;height:4301px;overflow:hidden}
body{font-family:"Plus Jakarta Sans",Arial,sans-serif;color:var(--ink);background:var(--paper);position:relative}
.btn{display:inline-flex;align-items:center;justify-content:center;font-size:11px;font-weight:600;border-radius:3px;text-decoration:none}
.btn-solid{background:var(--green);color:var(--white)}
.btn-outline{border:1.5px solid var(--white);color:var(--white)}
.abs{position:absolute}

/* hero */
.hero{position:absolute;top:0;left:0;width:1200px;height:537px;background:linear-gradient(180deg,#35513a 0%,#4c6e58 35%,#3f7a80 60%,#2f5a4e 100%)}
.hero-shade{position:absolute;inset:0;background:rgba(20,35,25,.35)}
.hero-phone{left:200px;top:45px;color:#fff;font-size:13px;font-weight:600;display:flex;gap:6px;align-items:center}
.brand{left:500px;top:22px;width:200px;text-align:center;color:#fff}
.brand-mark{width:30px;height:30px;border-radius:50%;background:#fff;margin:0 auto 8px}
.brand-name{font-size:15px;font-weight:500;letter-spacing:.5px}
.hero-book{left:886px;top:37px;width:114px;height:37px}
.hero-title{left:150px;top:200px;width:900px;text-align:center;color:#fff;font-size:29px;font-weight:300;line-height:37px}
.hero-title b{font-weight:700}
.hero-contact{left:544px;top:339px;width:112px;height:34px}

.booking{left:162px;top:472px;width:876px;height:112px;background:#fff;border-radius:8px;box-shadow:0 6px 18px rgba(0,0,0,.1);padding:28px 38px 0 38px;display:flex;gap:12px;align-items:flex-start;z-index:2}
.field{display:flex;flex-direction:column;gap:8px}
.field label{font-size:9px;font-weight:600;color:#444}
.field .box{height:37px;border:1px solid #d8d8d8;border-radius:3px;display:flex;align-items:center;justify-content:space-between;padding:0 10px;font-size:11px;color:#444}
.booking .btn{margin-top:21px;width:150px;height:37px}

/* bonus */
.bonus{position:absolute;top:537px;left:0;width:1200px;height:613px;background:var(--green)}
.bonus h2{position:absolute;top:115px;left:0;width:1200px;text-align:center;color:#fff;font-size:28px;font-weight:400;line-height:37px}
.card{position:absolute;top:222px;width:250px;height:206px;background:#fff;border-radius:4px;overflow:hidden}
.card .photo{height:155px}
.card p{text-align:center;font-size:17px;line-height:51px;color:#222}
.bonus .fine{position:absolute;top:456px;width:1200px;text-align:center;font-size:10px;color:#fff}
.bonus .btn{position:absolute;left:543px;top:501px;width:114px;height:39px}

/* why */
.why{position:absolute;top:1150px;left:0;width:1200px;height:490px;background:linear-gradient(90deg,#f3f4f2 0%,#eef0ee 55%,#d5dccf 75%,#a9c08a 100%)}
.why-photo{position:absolute;right:0;top:0;width:520px;height:490px;background:linear-gradient(160deg,rgba(255,255,255,0) 10%,rgba(120,160,80,.55) 55%,rgba(60,110,45,.8) 100%)}
.why h2{position:absolute;left:200px;top:68px;font-size:29px;font-weight:400;color:#333}
.why ul{position:absolute;left:200px;top:120px;width:600px;list-style:none}
.why li{position:relative;padding-left:22px;font-size:11.5px;font-weight:600;color:#555;line-height:19px;margin-bottom:18px}
.why li svg{position:absolute;left:0;top:3px}
.why .btn{position:absolute;left:200px;top:372px;width:113px;height:38px}
.rule{position:absolute;top:1640px;left:0;width:1200px;height:3px;background:var(--green)}

/* reviews */
.reviews{position:absolute;top:1643px;left:0;width:1200px;height:522px;background:var(--paper)}
.reviews h2{position:absolute;top:68px;width:1200px;text-align:center;font-size:29px;font-weight:400;color:#333}
.rating{position:absolute;top:114px;width:1200px;display:flex;justify-content:center;align-items:center;gap:6px;font-size:11px;color:#666}
.rating .dot{width:16px;height:16px;border-radius:50%;background:#2a2a2a}
.rating strong{color:#222;font-size:12px}
.rating .stars{color:var(--star);letter-spacing:1px}
.arrow{position:absolute;top:231px}
.review{position:absolute;top:166px;width:250px;height:147px;background:#fff;border-radius:3px;box-shadow:0 2px 8px rgba(0,0,0,.06);padding:18px 18px}
.review .stars{color:var(--star);font-size:11px;letter-spacing:2px}
.review h3{font-size:10.5px;font-weight:700;line-height:18px;margin-top:4px}
.review p{font-size:10.5px;line-height:18px;color:#444}
.review p span{color:var(--green)}
.author{position:absolute;top:343px;display:flex;gap:12px;align-items:center}
.author .av{width:36px;height:36px;border-radius:50%;background:linear-gradient(135deg,#c28a5a,#5a7aa0)}
.author b{display:block;font-size:10.5px;font-weight:600;color:#555}
.author small{font-size:9px;color:#888}
.reviews .btn{position:absolute;left:543px;top:408px;width:114px;height:38px}

/* gallery */
.gallery{position:absolute;top:2165px;left:0;width:1200px;height:794px;background:var(--paper)}
.g{position:absolute}
.play{position:absolute;left:50%;top:50%;width:62px;height:62px;margin:-31px 0 0 -31px;border:2px solid #fff;border-radius:50%;background:rgba(0,0,0,.15)}
.play:after{content:"";position:absolute;left:24px;top:19px;border-left:18px solid #fff;border-top:11px solid transparent;border-bottom:11px solid transparent}

/* facilities */
.facilities{position:absolute;top:2959px;left:0;width:1200px;height:654px;background:var(--paper)}
.facilities h2{position:absolute;top:70px;width:1200px;text-align:center;font-size:30px;font-weight:600;color:var(--green-dark)}
.facilities h3{position:absolute;top:108px;width:1200px;text-align:center;font-size:28px;font-weight:400;color:#333}
.tile{position:absolute;top:174px;width:137px;height:135px;background:#fff;border-radius:3px;text-align:center;padding-top:28px}
.tile p{font-size:11px;line-height:15px;color:#555;margin-top:10px}
.callus{position:absolute;top:339px;width:1200px;text-align:center;font-size:18px;color:#333}
.facilities .btn{position:absolute;left:543px;top:391px;width:114px;height:38px}
.badge{position:absolute;top:505px;height:70px;display:flex;align-items:center}

/* map & contact */
.map{position:absolute;top:3613px;left:0;width:1200px;height:217px;background:linear-gradient(180deg,#cfe0c9 0%,#e4ecdc 60%,#d8e6d2 100%)}
.lower{position:absolute;top:3830px;left:0;width:1200px;height:471px;background:var(--green-foot)}
.contact{position:absolute;top:3762px;left:200px;width:800px;height:410px;display:flex;z-index:2}
.contact-info{width:400px;background:var(--green-deep);color:#fff;padding:58px 0 0 67px}
.contact-info h2{font-size:18px;font-weight:400;margin-bottom:26px}
.ci{display:flex;gap:10px;align-items:center;font-size:15px;line-height:23px}
.ci.sm{font-size:11px;line-height:16px;margin-top:18px;align-items:flex-start}
.dirs{margin-top:30px;width:126px;height:37px;border:1.5px solid #fff;color:#fff;font-size:11px;font-weight:600;display:flex;align-items:center;justify-content:center;border-radius:3px}
.social{display:flex;gap:8px;margin-top:38px}
.social span{width:30px;height:30px;border-radius:50%;background:#8bc34a}
.contact-form{width:400px;background:var(--paper);padding:58px 0 0 68px}
.contact-form h2{font-size:18px;font-weight:400;color:#333;margin-bottom:26px}
.in{width:262px;height:30px;background:#fff;border-radius:2px;font-size:9px;font-weight:600;color:#555;padding:10px 12px;margin-bottom:13px}
.in.tall{height:60px}
.contact-form .btn{width:88px;height:32px;margin-top:2px}
.foot-brand{position:absolute;top:4194px;left:500px;width:200px;text-align:center;color:#fff}
.foot-brand .brand-mark{width:22px;height:22px;margin-bottom:6px}
.foot-brand .brand-name{font-size:12px}
.copy{position:absolute;top:4264px;width:1200px;text-align:center;color:#fff;font-size:9px}
</style>
</head>
<body>

<header class="hero">
  <div role="img" aria-label="Resort pool terrace with loungers under tropical trees" class="hero-shade"></div>
  <div class="abs hero-phone">
    <svg width="12" height="12" viewBox="0 0 24 24" fill="none" stroke="#fff" stroke-width="2"><path d="M22 16.9v3a2 2 0 0 1-2.2 2 19.8 19.8 0 0 1-8.6-3.1 19.5 19.5 0 0 1-6-6A19.8 19.8 0 0 1 2.1 4.2 2 2 0 0 1 4.1 2h3a2 2 0 0 1 2 1.7c.1 1 .4 1.9.7 2.8a2 2 0 0 1-.5 2.1L8 9.9a16 16 0 0 0 6 6l1.3-1.3a2 2 0 0 1 2.1-.4c.9.3 1.8.6 2.8.7a2 2 0 0 1 1.7 2z"/></svg>
    (555) 318-2047
  </div>
  <div class="abs brand"><div class="brand-mark"></div><div class="brand-name">BRISA MARENA</div></div>
  <a class="abs btn btn-outline hero-book">Book Now!</a>
  <h1 class="abs hero-title"><b>Book a 4 Night Stay</b> During the Costa Rican Green-Season,<br>and <b>Get Your 5th Night Free</b> at this all Inclusive<br>Luxury Beachfront Resort!</h1>
  <a class="abs btn btn-solid hero-contact">Contact Us</a>
</header>

<form class="abs booking">
  <div class="field" style="width:163px"><label>Check-in</label><div class="box">1-11-2024 <svg width="10" height="10" viewBox="0 0 10 10"><rect x="1" y="2" width="8" height="7" fill="none" stroke="#666"/><line x1="1" y1="4" x2="9" y2="4" stroke="#666"/></svg></div></div>
  <div class="field" style="width:163px"><label>Check-out</label><div class="box">1-14-2024 <svg width="10" height="10" viewBox="0 0 10 10"><rect x="1" y="2" width="8" height="7" fill="none" stroke="#666"/><line x1="1" y1="4" x2="9" y2="4" stroke="#666"/></svg></div></div>
  <div class="field" style="width:87px"><label>Rooms</label><div class="box">1 <span style="font-size:7px">▼</span></div></div>
  <div class="field" style="width:87px"><label>Adults</label><div class="box">2 <span style="font-size:7px">▼</span></div></div>
  <div class="field" style="width:87px"><label>Children</label><div class="box">1 <span style="font-size:7px">▼</span></div></div>
  <a class="btn btn-solid">Book Now!</a>
</form>

<section class="bonus">
  <h2>As a bonus, we'll throw in any of these activities or tours<br>for free! Don't wait! These will fill up fast.</h2>
  <div class="card" style="left:200px"><div class="photo" role="img" aria-label="Guest receiving a massage by the sea" style="background:linear-gradient(180deg,#b9cbd8,#e6e2dc)"></div><p>Free Massage</p></div>
  <div class="card" style="left:476px"><div class="photo" role="img" aria-label="Caiman in dark water on a night hike" style="background:radial-gradient(circle at 50% 55%,#3f4a1c,#0d1208 70%)"></div><p>Night Hike</p></div>
  <div class="card" style="left:751px"><div class="photo" role="img" aria-label="Bird perched among berries" style="background:linear-gradient(135deg,#3d5a3a,#7a8f6a 55%,#2c4a6a)"></div><p>Birdwatching Tour</p></div>
  <p class="fine">*Max 2 per booking, can mix-match. While supplies last. Must redeemed during this stay.</p>
  <a class="btn btn-outline">Book Now!</a>
</section>

<section class="why">
  <div class="why-photo" role="img" aria-label="Palm trees over a misty tropical coastline"></div>
  <h2>Why choose us</h2>
  <ul>
    <li><svg width="12" height="10" viewBox="0 0 12 10"><path d="M1 5l3.5 3.5L11 1" fill="none" stroke="#2f7a36" stroke-width="1.6"/></svg>Accessible only via boat, this Costa Rican Luxury Paradise is perfect for those wanting to escape the crowds, enjoy amazing cuisine, while swimming in our beachfront pool, and more</li>
    <li><svg width="12" height="10" viewBox="0 0 12 10"><path d="M1 5l3.5 3.5L11 1" fill="none" stroke="#2f7a36" stroke-width="1.6"/></svg>Green Season is known for whale migrations, enjoy watching the marine life from our beachfront location, or up close and personal via kayak or paddleboard</li>
    <li><svg width="12" height="10" viewBox="0 0 12 10"><path d="M1 5l3.5 3.5L11 1" fill="none" stroke="#2f7a36" stroke-width="1.6"/></svg>Paddleboards, kayaks, snorkeling gear, and more are free during your stay.</li>
    <li><svg width="12" height="10" viewBox="0 0 12 10"><path d="M1 5l3.5 3.5L11 1" fill="none" stroke="#2f7a36" stroke-width="1.6"/></svg>Enjoy fresh cuisine and unique beverages daily.</li>
    <li><svg width="12" height="10" viewBox="0 0 12 10"><path d="M1 5l3.5 3.5L11 1" fill="none" stroke="#2f7a36" stroke-width="1.6"/></svg>Skyvane Internet Access Included with all Bookings.</li>
  </ul>
  <a class="btn btn-solid">Book Now!</a>
</section>
<div class="rule"></div>

<section class="reviews">
  <h2>Customer reviews</h2>
  <div class="rating"><span class="dot"></span><strong>TripVista</strong> Rating <strong>5.0</strong> <span class="stars">★★★★★</span> 643 reviews</div>
  <svg class="arrow" style="left:148px" width="12" height="16" viewBox="0 0 12 16"><path d="M9 2L3 8l6 6" fill="none" stroke="#444" stroke-width="2"/></svg>
  <svg class="arrow" style="left:1040px" width="12" height="16" viewBox="0 0 12 16"><path d="M3 2l6 6-6 6" fill="none" stroke="#444" stroke-width="2"/></svg>
  <article class="review" style="left:200px"><div class="stars">★★★★★</div><h3>A spectacular resort -- Castaway Cove on Steroids!!</h3><p>We had an absolutely superb experience staying at this resort. The facility is beautifully <span>[ More... ]</span></p></article>
  <article class="review" style="left:476px"><div class="stars">★★★★★</div><h3>perfect vacation</h3><p>My husband and I just returned from a fabulous week at Brisa Marena. Everything was perfect <span>[ More... ]</span></p></article>
  <article class="review" style="left:751px"><div class="stars">★★★★★</div><h3>Memories to last a lifetime!</h3><p>Amazing! Inspiring! We were a large family group (ages 4-76!) and Brisa Marena was <span>[ More... ]</span></p></article>
  <div class="author" style="left:226px"><div class="av"></div><div><b>Lorna</b><small>January 1</small></div></div>
  <div class="author" style="left:501px"><div class="av"></div><div><b>Dana Pell</b><small>December 31, 2023</small></div></div>
  <div class="author" style="left:776px"><div class="av"></div><div><b>Mirelle K</b><small>December 31, 2023</small></div></div>
  <a class="btn btn-solid">View All</a>
</section>

<section class="gallery">
  <div class="g" role="img" aria-label="Video: aerial view of the beach and rainforest" style="left:0;top:0;width:596px;height:343px;background:linear-gradient(160deg,#3d6a30,#6b8a45 45%,#4e8fa0 75%,#2c6a8a)"><span class="play"></span></div>
  <div class="g" role="img" aria-label="Video: infinity pool among jungle" style="left:602px;top:0;width:598px;height:343px;background:linear-gradient(180deg,#2e4a2a,#4a7a5a 45%,#6ab8c8 75%,#2a3a2a)"><span class="play"></span></div>
  <div class="g" role="img" aria-label="Guest relaxing by the pool" style="left:0;top:350px;width:380px;height:217px;background:linear-gradient(135deg,#4a6a3a,#7ab0c0 55%,#c09060)"></div>
  <div class="g" role="img" aria-label="Turquoise cove and forested point" style="left:387px;top:350px;width:306px;height:217px;background:linear-gradient(180deg,#8ab8d8,#5a8a4a 40%,#3a9aa0 75%,#2a7a8a)"></div>
  <div class="g" role="img" aria-label="Ocean view dining deck" style="left:699px;top:350px;width:251px;height:217px;background:linear-gradient(180deg,#3a5a3a,#6aa0c0 50%,#3a4a3a)"></div>
  <div class="g" role="img" aria-label="Wooden bungalow in the jungle" style="left:956px;top:350px;width:244px;height:217px;background:linear-gradient(180deg,#5a8a4a,#3a6a30 60%,#9a8a70)"></div>
  <div class="g" role="img" aria-label="Thatched cabin in gardens" style="left:0;top:574px;width:244px;height:220px;background:linear-gradient(180deg,#c8d0c8,#6a7a50 50%,#3a5a2a)"></div>
  <div class="g" role="img" aria-label="Paddleboarding on calm water" style="left:250px;top:574px;width:251px;height:220px;background:linear-gradient(180deg,#5a8aa0,#3a7a90 60%,#2a6a80)"></div>
  <div class="g" role="img" aria-label="Sloth in a tree" style="left:507px;top:574px;width:306px;height:220px;background:linear-gradient(135deg,#2a6a2a,#5a9a3a 50%,#8a7a5a)"></div>
  <div class="g" role="img" aria-label="Tropical drink by the beach" style="left:819px;top:574px;width:381px;height:220px;background:linear-gradient(135deg,#4ab8d0,#8ad0e0 50%,#e8c070)"></div>
</section>

<section class="facilities">
  <h2>Facilities</h2>
  <h3>Book your stay with us today</h3>
  <div class="tile" style="left:82px"><svg width="36" height="36" viewBox="0 0 36 36" fill="none" stroke="#2f7a36" stroke-width="1.6"><rect x="8" y="18" width="20" height="12"/><path d="M12 12a9 9 0 0 1 12 0M15 15a4 4 0 0 1 6 0"/></svg><p>Free Wi-fi</p></div>
  <div class="tile" style="left:232px"><svg width="36" height="36" viewBox="0 0 36 36" fill="none" stroke="#2f7a36" stroke-width="1.6"><path d="M11 12h14l-2 18H13z"/><path d="M18 12V5"/></svg><p>Minibar</p></div>
  <div class="tile" style="left:382px"><svg width="36" height="36" viewBox="0 0 36 36" fill="none" stroke="#2f7a36" stroke-width="1.6"><path d="M5 24h26l-4 6H9z"/><rect x="11" y="14" width="14" height="10"/><path d="M18 8v6M4 33h28"/></svg><p>Shuttle Boat<br>Service</p></div>
  <div class="tile" style="left:532px"><svg width="36" height="36" viewBox="0 0 36 36" fill="none" stroke="#2f7a36" stroke-width="1.6"><rect x="6" y="20" width="24" height="11"/><rect x="12" y="6" width="12" height="10"/><path d="M18 16v4"/></svg><p>24-Hours Front<br>Desk</p></div>
  <div class="tile" style="left:682px"><svg width="36" height="36" viewBox="0 0 36 36" fill="none" stroke="#2f7a36" stroke-width="1.6"><rect x="6" y="8" width="24" height="22" rx="2"/><path d="M6 14h24M12 5v6M24 5v6"/><rect x="12" y="19" width="4" height="4"/></svg><p>Check-In<br>11:00 am</p></div>
  <div class="tile" style="left:832px"><svg width="36" height="36" viewBox="0 0 36 36" fill="none" stroke="#2f7a36" stroke-width="1.6"><circle cx="18" cy="18" r="12"/><path d="M18 10v8h6"/></svg><p>Check-Out<br>9:00 am</p></div>
  <div class="tile" style="left:982px"><svg width="36" height="36" viewBox="0 0 36 36" fill="none" stroke="#2f7a36" stroke-width="1.6"><circle cx="18" cy="18" r="12"/><path d="M10 10l16 16M9 20h15"/></svg><p>100% Smoke<br>Free</p></div>
  <p class="callus">Call Us
    <svg width="14" height="14" viewBox="0 0 24 24" fill="none" stroke="#2f7a36" stroke-width="2"><path d="M22 16.9v3a2 2 0 0 1-2.2 2 19.8 19.8 0 0 1-8.6-3.1 19.5 19.5 0 0 1-6-6A19.8 19.8 0 0 1 2.1 4.2 2 2 0 0 1 4.1 2h3a2 2 0 0 1 2 1.7c.1 1 .4 1.9.7 2.8a2 2 0 0 1-.5 2.1L8 9.9a16 16 0 0 0 6 6l1.3-1.3a2 2 0 0 1 2.1-.4c.9.3 1.8.6 2.8.7a2 2 0 0 1 1.7 2z"/></svg>
    (555) 318-2047</p>
  <a class="btn btn-solid">Book Now!</a>
  <div class="badge" style="left:162px"><svg width="60" height="70"><circle cx="30" cy="32" r="26" fill="#d9d9d6"/></svg></div>
  <div class="badge" style="left:276px"><svg width="140" height="40"><rect width="140" height="40" rx="4" fill="#cfdccc"/></svg></div>
  <div class="badge" style="left:470px"><svg width="60" height="70"><circle cx="30" cy="32" r="26" fill="#d9d9d6"/></svg></div>
  <div class="badge" style="left:594px"><svg width="130" height="30"><rect width="130" height="30" rx="4" fill="#f0d2c8"/></svg></div>
  <div class="badge" style="left:762px"><svg width="105" height="50"><rect width="105" height="50" rx="4" fill="#d4e2cf"/></svg></div>
  <div class="badge" style="left:910px"><svg width="128" height="30"><rect width="128" height="30" rx="4" fill="#d2d8e8"/></svg></div>
</section>

<div class="map" role="img" aria-label="Map of the coast showing the resort location"></div>
<div class="lower"></div>

<section class="contact">
  <div class="contact-info">
    <h2>Contact Us</h2>
    <div class="ci"><svg width="12" height="12" viewBox="0 0 24 24" fill="none" stroke="#fff" stroke-width="2"><path d="M22 16.9v3a2 2 0 0 1-2.2 2A19.8 19.8 0 0 1 2.1 4.2 2 2 0 0 1 4.1 2h3l2 5-2.5 2.5a16 16 0 0 0 8 8L17 15l5 1.9z"/></svg>555-7142-0938</div>
    <div class="ci"><svg width="12" height="12" viewBox="0 0 24 24" fill="none" stroke="#fff" stroke-width="2"><path d="M22 16.9v3a2 2 0 0 1-2.2 2A19.8 19.8 0 0 1 2.1 4.2 2 2 0 0 1 4.1 2h3l2 5-2.5 2.5a16 16 0 0 0 8 8L17 15l5 1.9z"/></svg>555-318-2047</div>
    <div class="ci sm"><svg width="12" height="12" viewBox="0 0 24 24" fill="none" stroke="#fff" stroke-width="2"><rect x="2" y="5" width="20" height="14"/><path d="M2 5l10 8 10-8"/></svg>info@brisamarena.com</div>
    <div class="ci sm"><svg width="12" height="12" viewBox="0 0 24 24" fill="#fff"><path d="M12 2a7 7 0 0 0-7 7c0 5 7 13 7 13s7-8 7-13a7 7 0 0 0-7-7zm0 9.5A2.5 2.5 0 1 1 12 6.5a2.5 2.5 0 0 1 0 5z"/></svg><span>Brisa Marena:<br>Bahía Serena, Punta Coral, Costa Rica</span></div>
    <div class="dirs">Get Directions</div>
    <div class="social"><span></span><span></span><span></span><span></span><span></span><span></span></div>
  </div>
  <form class="contact-form">
    <h2>Send Us a Message</h2>
    <div class="in">Your Name</div>
    <div class="in">Email</div>
    <div class="in">Phone</div>
    <div class="in">Subject</div>
    <div class="in tall">Message ...</div>
    <a class="btn btn-solid">Submit</a>
  </form>
</section>

<footer>
  <div class="foot-brand"><div class="brand-mark"></div><div class="brand-name">BRISA MARENA</div></div>
  <p class="copy">© 2024 Brisa Marena. All Right Reserved</p>
</footer>

</body>
</html>
```